Need to create logo for Brightwell Designs Ltd

We supply the above mention products all around NZ. Trading under the company name Brightwell Designs Ltd.

Industry/Entity Type

It Company

Contact Information for Business Card

Brightwell Designs Ltd. 0800519203 0274095162 Trevor@Solvane.co.nz contact Trevor HOLT
Suppliers of Solvane Louvres, Metrofold Clear shutters, Glidemesh curtains,Emberline outdoor heaters,Calvor outdoor heaters

```html
<!DOCTYPE html>
<html lang="en">
<head>
<meta charset="utf-8">
<title>Brightwell Designs Ltd — Business Card</title>
<link rel="stylesheet" href="https://fonts.googleapis.com/css2?family=Tinos:wght@400;700&family=Arimo:wght@400&display=swap">
<style>
  :root {
    --page-bg: #3a322e;
    --card-bg: #141414;
    --card-edge: #1e1e1e;
    --gold-light: #e8c15a;
    --gold-mid: #b8862a;
    --gold-dark: #6e4a12;
    --ink-white: #f4f4f4;
    --ink-soft: #e6e6e6;
  }
  html, body {
    margin: 0;
    padding: 0;
    width: 1200px;
    height: 780px;
    overflow: hidden;
    background: var(--page-bg);
  }
  .stage {
    width: 1200px;
    height: 780px;
    display: flex;
    align-items: center;
    justify-content: center;
    gap: 48px;
  }
  .card {
    position: relative;
    width: 520px;
    height: 300px;
    background: var(--card-bg);
    border: 1px solid var(--card-edge);
    border-radius: 3px;
    box-shadow: 0 14px 30px rgba(0,0,0,0.45);
    overflow: hidden;
  }
  /* Front */
  .card-front {
    display: flex;
    align-items: center;
    justify-content: center;
  }
  .front-name {
    font-family: "Tinos", serif;
    font-weight: 700;
    font-size: 38px;
    letter-spacing: 0.5px;
    background: linear-gradient(180deg, var(--gold-light) 0%, var(--gold-mid) 55%, var(--gold-dark) 100%);
    -webkit-background-clip: text;
    background-clip: text;
    color: transparent;
  }
  /* Back */
  .back-title {
    position: absolute;
    right: 36px;
    top: 52px;
    margin: 0;
    font-family: "Tinos", serif;
    font-weight: 700;
    font-size: 34px;
    color: var(--ink-white);
    letter-spacing: 0.5px;
  }
  .back-rule {
    position: absolute;
    left: 0;
    right: 22px;
    top: 106px;
    height: 1.5px;
    background: var(--ink-white);
  }
  .contact-name {
    position: absolute;
    left: 88px;
    top: 128px;
    margin: 0;
    font-family: "Tinos", serif;
    font-weight: 700;
    font-size: 23px;
    color: var(--ink-white);
    letter-spacing: 0.5px;
  }
  .contact-list {
    position: absolute;
    left: 62px;
    top: 176px;
    margin: 0;
    padding: 0;
    list-style: none;
    font-family: "Arimo", sans-serif;
    font-size: 16px;
    color: var(--ink-soft);
  }
  .contact-list li {
    display: flex;
    align-items: center;
    gap: 12px;
    height: 25px;
  }
  .contact-icon {
    width: 14px;
    height: 14px;
    flex: none;
  }
</style>
</head>
<body>
  <main class="stage">
    <section class="card card-front" aria-label="Card front">
      <span class="front-name">Brightwell Designs Ltd</span>
    </section>

    <section class="card card-back" aria-label="Card back">
      <h1 class="back-title">Brightwell Designs Ltd</h1>
      <div class="back-rule"></div>
      <h2 class="contact-name">Trevor HOLT</h2>
      <ul class="contact-list">
        <li>
          <svg class="contact-icon" viewBox="0 0 14 14" aria-hidden="true">
            <rect width="14" height="14" rx="1.5" fill="#f4f4f4"/>
            <path d="M3 4.5 Q7 2 11 4.5 L10 6 L8.5 5.3 L8.5 6.3 L5.5 6.3 L5.5 5.3 L4 6 Z" fill="#141414"/>
            <rect x="4" y="7" width="6" height="4" rx="0.5" fill="#141414"/>
          </svg>
          <span>0800 519 203</span>
        </li>
        <li>
          <svg class="contact-icon" viewBox="0 0 14 14" aria-hidden="true">
            <rect width="14" height="14" rx="1.5" fill="#f4f4f4"/>
            <rect x="4.5" y="2.5" width="5" height="9" rx="0.8" fill="#141414"/>
            <rect x="5.3" y="3.6" width="3.4" height="5.4" fill="#f4f4f4"/>
          </svg>
          <span>0274 095 162</span>
        </li>
        <li>
          <svg class="contact-icon" viewBox="0 0 14 14" aria-hidden="true">
            <rect width="14" height="14" rx="1.5" fill="#f4f4f4"/>
            <rect x="2.5" y="4" width="9" height="6.5" fill="#141414"/>
            <path d="M2.8 4.3 L7 7.6 L11.2 4.3" stroke="#f4f4f4" stroke-width="0.9" fill="none"/>
          </svg>
          <span>Trevor@Solvane.co.nz</span>
        </li>
      </ul>
    </section>
  </main>
</body>
</html>
```